Bref créative
Modern Creative Stationary for Tech Start up!!!
TheByteDepot - Business cards - Letterheads - Email Signature -
Use same font as used in my logo
Smaller Text can be different- but in line with theme.
Professional
Pavel Orsk
Client Accounts
5th Floor Birch Court
7X Fernhill Street
Ashmere
London
HBX 8QW
0208 731 XXXX
07452168XXX
pavel@thebytedepotz.com
thebytedepotz.com
We want a double sided Business card that is elegant, modern, sleek and also creative. The logo should give you an idea of where we want to go in terms of theme.
Be creative, Be sexy and try your hardest as there is plenty more work to be done after this project.
This is our Logo.
We do not really like the shaded background. So it might be best to keep it flat black.
This is the white version of our Logo. It may be an idea to use this for the stationary.

```html
<!DOCTYPE html>
<html lang="en">
<head>
<meta charset="utf-8">
<title>TheByteDepot – Business Card</title>
<link href="https://fonts.googleapis.com/css2?family=Montserrat:wght@400;500;700;800&display=swap" rel="stylesheet">
<style>
  :root{
    --stage:#e4e4e4;
    --card:#0d0d0d;
    --card-edge:#1c1c1c;
    --strip:#f1f1f1;
    --strip-text:#1e1e1e;
    --ink:#ffffff;
    --ink-soft:#bdbdbd;
    --orange:#f28a1e;
    --blue:#2a9fd8;
    --green:#7cbf3a;
  }
  *{margin:0;padding:0;box-sizing:border-box}
  html,body{width:1200px;height:874px;overflow:hidden}
  body{background:var(--stage);font-family:"Montserrat",sans-serif;position:relative}

  .card{
    position:absolute;top:277px;width:555px;height:320px;
    background:linear-gradient(160deg,var(--card-edge),var(--card) 45%);
    border-radius:22px;overflow:hidden;
  }
  .card--details{left:30px}
  .card--brand{left:615px}

  .web-strip{
    position:absolute;left:0;right:0;bottom:0;height:58px;
    background:var(--strip);display:flex;align-items:center;padding-left:30px;
    font-weight:700;font-size:19px;color:var(--strip-text);letter-spacing:.2px;
  }
  .edge-tabs{position:absolute;right:0;top:104px;width:34px;display:flex;flex-direction:column;gap:5px}
  .edge-tabs span{display:block;height:30px;border-radius:6px 0 0 6px}
  .edge-tabs .tab-top{background:var(--strip);height:56px}
  .tab-orange{background:var(--orange)}
  .tab-blue{background:var(--blue)}
  .tab-green{background:var(--green)}

  .brand{position:absolute;display:flex;align-items:center;gap:14px}
  .brand__dot{width:46px;height:46px;border-radius:50%;background:var(--blue)}
  .brand__name{font-weight:800;color:var(--ink);font-size:38px;letter-spacing:-.5px}
  .card--brand .brand{left:70px;top:108px}
  .card--details .brand{left:30px;top:150px}
  .card--details .brand__dot{width:30px;height:30px}
  .card--details .brand__name{font-size:24px}

  .contact{position:absolute;right:52px;top:32px;text-align:right;color:var(--ink)}
  .contact__name{font-weight:700;font-size:21px}
  .contact__role{font-size:11px;color:var(--ink-soft);margin-bottom:14px}
  .contact__line{font-size:11px;line-height:1.5;color:var(--ink-soft)}
  .contact__list{margin-top:10px;list-style:none}
  .contact__list li{font-size:11px;line-height:1.75;color:var(--ink);display:flex;justify-content:flex-end;align-items:center;gap:7px}
  .contact__list svg{width:11px;height:11px;fill:var(--ink-soft)}
</style>
</head>
<body>

<section class="card card--details">
  <div class="contact">
    <p class="contact__name">Pavel Orsk</p>
    <p class="contact__role">Client Accounts</p>
    <p class="contact__line">5th Floor Birch Court</p>
    <p class="contact__line">7X Fernhill Street, Ashmere</p>
    <p class="contact__line">London HBX 8QW</p>
    <ul class="contact__list">
      <li>0208 731 XXXX
        <svg viewBox="0 0 24 24"><path d="M6.6 10.8a15 15 0 0 0 6.6 6.6l2.2-2.2a1 1 0 0 1 1-.25 11.4 11.4 0 0 0 3.6.57 1 1 0 0 1 1 1V20a1 1 0 0 1-1 1A17 17 0 0 1 3 4a1 1 0 0 1 1-1h3.5a1 1 0 0 1 1 1c0 1.25.2 2.45.57 3.57a1 1 0 0 1-.25 1z"/></svg></li>
      <li>07452168XXX
        <svg viewBox="0 0 24 24"><path d="M7 1h10a2 2 0 0 1 2 2v18a2 2 0 0 1-2 2H7a2 2 0 0 1-2-2V3a2 2 0 0 1 2-2zm0 3v14h10V4zm5 15.5a1 1 0 1 0 0 2 1 1 0 0 0 0-2z"/></svg></li>
      <li>pavel@thebytedepotz.com
        <svg viewBox="0 0 24 24"><path d="M2 5h20v14H2zm2 2v.5l8 5 8-5V7zm0 2.8V17h16V9.8l-8 5z"/></svg></li>
    </ul>
  </div>
  <div class="brand">
    <span class="brand__dot"></span>
    <span class="brand__name">TheByteDepot</span>
  </div>
  <div class="edge-tabs">
    <span class="tab-top"></span>
    <span class="tab-orange"></span>
    <span class="tab-blue"></span>
    <span class="tab-green"></span>
  </div>
  <div class="web-strip">www.thebytedepotz.com</div>
</section>

<section class="card card--brand">
  <div class="brand">
    <span class="brand__dot"></span>
    <span class="brand__name">TheByteDepot</span>
  </div>
  <div class="edge-tabs">
    <span class="tab-top"></span>
    <span class="tab-orange"></span>
    <span class="tab-blue"></span>
    <span class="tab-green"></span>
  </div>
  <div class="web-strip">www.thebytedepotz.com</div>
</section>

</body>
</html>
```